Postcard double sided

Title: DWIGHT'S REVENGE

Why would Dwight Kessler align himself with Gordon Pruett?

(photo of two guys)

Dwight approached elected officials that he wanted to run for office, but did not have money to finance his campaign. He wanted other elected officials to finance his campaign. Everyone told him that they would help him get the vote out, but that he needed to finance his own race.

In comes Gordon Pruett.

Gordon Pruett who has a pay to play scheme over at the City, told Dwight he would finance his campaign on one condition.

He needed to run against Steven Hulse.

Why would Dwight want to run with no money?

Backside

DWIGHT'S REVENGE

Dwight decided to run because no one on the school board would terminate Dwight's ex and her new boyfriend who both work for the school district. His ex even filed criminal charges against him that are still pending.

Mug Shot facing left (name the charges Criminal Trespass , and Criminal Mischief (highlight bold letters use two lines) mug shot facing right

Complaint one (then photo with full face) Compliant 2)
(showcharges)

Dwight's ultimate goal is to terminate his ex and her new boyfriend if elected.
Plus Gordon Pruett needs the majority on the school board to do what he does bet.

Kickbacks for Contracts.

They will hire their own contractors!
Say "No" to Dwight's Revenge and Gordon Pruett Money Grab!

Title On Back: all caps: DOMESTIC VIOLENCE

```html
<!DOCTYPE html>
<html lang="en">
<head>
<meta charset="utf-8">
<title>Dwight's Revenge – Postcard</title>
<link rel="stylesheet" href="https://fonts.googleapis.com/css2?family=Archivo+Black&family=Comic+Neue:wght@400;700&family=Arimo:wght@400;700&display=swap">
<style>
  :root {
    --ink-blue: #2a5ba8;
    --deep-blue: #1d4c9c;
    --mid-blue: #1f6ec0;
    --bright-blue: #1aa0e0;
    --panel-grey: #4a4a4c;
    --photo-dark: #2e2f34;
    --photo-skin: #a88c7a;
    --rule-grey: #555;
    --label-grey: #333;
    --white: #ffffff;
    --frame: #9a9a9a;
  }
  * { box-sizing: border-box; margin: 0; padding: 0; }
  html, body { width: 852px; height: 1200px; overflow: hidden; background: var(--white); }
  .sheet {
    position: relative; width: 852px; height: 1200px;
    border: 1px solid var(--frame);
    font-family: "Comic Neue", "Comic Sans MS", cursive;
  }
  .card {
    position: absolute; left: 43px; width: 768px; height: 512px;
    border: 1px solid var(--frame); overflow: hidden; background: var(--white);
  }
  .card--front { top: 37px; }
  .card--back { top: 614px; }

  .side-label {
    position: absolute; left: 0; width: 852px; text-align: center;
    font-family: "Arimo", Arial, sans-serif; font-size: 28px; color: var(--label-grey);
  }
  .side-label--front { top: 559px; left: 17px; }
  .side-label--back { top: 1145px; left: 17px; }

  /* front */
  .front-swoosh { position: absolute; inset: 0; }
  .front-heading {
    position: absolute; left: 49px; top: 40px; width: 280px;
    font-family: "Arimo", Arial, sans-serif; font-weight: 700;
    font-size: 26px; line-height: 31px; color: var(--ink-blue);
  }
  .front-photo {
    position: absolute; left: 50px; top: 186px; width: 251px; height: 291px;
    background: linear-gradient(180deg, #2c3a6a 0%, #3a3a44 45%, #1f2026 100%);
  }
  .front-story {
    position: absolute; left: 439px; top: 40px; width: 305px;
    color: var(--white); font-size: 15px; line-height: 21px;
  }
  .front-story p + p { margin-top: 21px; }

  /* back */
  .back-edge { position: absolute; top: 0; bottom: 0; width: 15px; background: linear-gradient(180deg, var(--deep-blue), var(--bright-blue) 45%, var(--deep-blue)); }
  .back-edge--left { left: 0; }
  .back-edge--right { left: 480px; width: 20px; }
  .back-panel { position: absolute; left: 15px; top: 0; width: 465px; height: 512px; background: var(--panel-grey); }
  .back-photo {
    position: absolute; left: 250px; top: 0; width: 215px; height: 512px;
    background: linear-gradient(90deg, var(--panel-grey) 0%, #6d625c 30%, var(--photo-skin) 55%, #7a6a60 75%, var(--photo-dark) 100%);
  }
  .back-title {
    position: absolute; left: 24px; top: 26px;
    font-family: "Archivo Black", "Arial Black", sans-serif; color: var(--white);
    font-size: 38px; line-height: 38px; letter-spacing: 0.5px;
  }
  .back-subtitle {
    position: absolute; left: 276px; top: 42px;
    font-family: "Arimo", Arial, sans-serif; font-weight: 700; color: var(--white);
    font-size: 21px; line-height: 20px;
  }
  .back-subtitle span { display: block; font-size: 19px; }
  .back-story {
    position: absolute; left: 27px; top: 114px; width: 440px;
    color: var(--white); font-size: 14.5px; line-height: 21px;
  }
  .back-story p + p { margin-top: 19px; }
  .evidence {
    position: absolute; top: 363px; width: 114px; height: 149px;
    background: linear-gradient(180deg, #fbfbfb, #e9e9e9);
  }
  .evidence--one { left: 28px; }
  .evidence--two { left: 151px; }
  .back-callout {
    position: absolute; left: 295px; top: 370px; width: 185px; color: var(--white);
  }
  .back-callout p { font-size: 14px; line-height: 21px; }
  .back-callout strong {
    display: block; font-family: "Arimo", Arial, sans-serif; font-weight: 700;
    font-size: 18.5px; line-height: 21px;
  }
  .address-lines { position: absolute; left: 517px; top: 286px; width: 227px; }
  .address-lines span { display: block; height: 38px; border-bottom: 1px solid var(--rule-grey); }
</style>
</head>
<body>
<div class="sheet">

  <section class="card card--front">
    <svg class="front-swoosh" width="768" height="512" viewBox="0 0 768 512" aria-hidden="true">
      <defs>
        <radialGradient id="frontBlue" cx="0.55" cy="0.6" r="0.6">
          <stop offset="0" stop-color="#1aa0e0"/>
          <stop offset="1" stop-color="#1d4c9c"/>
        </radialGradient>
        <linearGradient id="silver" x1="0" y1="0" x2="1" y2="0">
          <stop offset="0" stop-color="#ffffff"/>
          <stop offset="1" stop-color="#c9ccd3"/>
        </linearGradient>
      </defs>
      <path d="M300 0 C360 120 370 340 255 512 L290 512 C380 360 385 140 340 0 Z" fill="url(#silver)"/>
      <path d="M312 0 C368 140 372 360 262 512 L768 512 L768 0 Z" fill="#1d4c9c"/>
      <path d="M372 0 C410 150 400 370 325 512 L342 512 C420 370 428 150 390 0 Z" fill="#ffffff"/>
      <path d="M390 0 C428 150 420 370 342 512 L768 512 L768 0 Z" fill="url(#frontBlue)"/>
    </svg>
    <h1 class="front-heading">Why would Dwight Kessler align himself with Gordon Pruett?</h1>
    <div class="front-photo" role="img" aria-label="Photo of Dwight Kessler and Gordon Pruett standing together at an event"></div>
    <div class="front-story">
      <p>Dwight approached elected officials that he wanted to run for office, but did not have money to finance his campaign. He wanted other elected officials to finance his campaign. Everyone told him that they would help him get the vote out, but that he needed to finance his own race.</p>
      <p>In comes Gordon Pruett.<br>Gordon Pruett who has a pay to play scheme over at the City, told Dwight he would finance his campaign on one condition.</p>
      <p>He needed to run against Steven Hulse.</p>
      <p>Why would Dwight want to run with no money?</p>
    </div>
  </section>
  <div class="side-label side-label--front">FRONT</div>

  <section class="card card--back">
    <div class="back-edge back-edge--left"></div>
    <div class="back-panel">
      <div class="back-photo" role="img" aria-label="Mug shot of Dwight Kessler"></div>
    </div>
    <div class="back-edge back-edge--right"></div>
    <h2 class="back-title">DOMESTIC<br>VIOLENCE</h2>
    <div class="back-subtitle">DWIGHT'S<span>REVENGE</span></div>
    <div class="back-story">
      <p>Dwight decided to run because no one on the school board would terminate Dwight's ex and her new boyfriend who both work for the school district. His ex even filed criminal charges against him that are still pending.</p>
      <p>Mug Shot facing left (name the charges Criminal Trespass , and Criminal Mischief (highlight bold letters use two lines) mug shot facing right</p>
      <p>Dwight's ultimate goal is to terminate his ex and her new boyfriend if elected. Plus Gordon Pruett needs the majority on the school board to do what he does bet.Kickbacks for Contracts.</p>
    </div>
    <div class="evidence evidence--one" role="img" aria-label="Criminal complaint document one"></div>
    <div class="evidence evidence--two" role="img" aria-label="Criminal complaint document two"></div>
    <div class="back-callout">
      <p>They will hire their own contractors!</p>
      <strong>Say "No" to Dwight's Revenge &amp; Gordon Pruett Money Grab!</strong>
    </div>
    <div class="address-lines"><span></span><span></span><span></span><span></span></div>
  </section>
  <div class="side-label side-label--back">BACK</div>

</div>
</body>
</html>
```